Wind Turbine Blade Repair Brochure

Design a new brochure for our relaunched company doing wind turbine blade services. We carry out rotor blade inspections & repairs to wind turbines.Most of the information can be taken from our old brochure but will need new company details, updated images & better design.
New company details are shown in the attached letterhead. Please use the Q8 Harlow Yard address & not the other. Website needs to be: www.fenmoor-lift.uk
Telephone: 020 7958 2316
E-mail: enquiries@fenmoor-lift.com
The other details in the letterhead do not need to be on the brochure
All references to "TOSK" need to change to "Fenmoor Lift"
I have included some additional images that can be used.

Target Market(s)

Wind turbine operators & manufacturers

Requirements
Must have
• All details listed in attached brochure
• Good layout of images
• Eye catching front page design that links well with our logo & industry
Nice to have
• Bar code scan to website / LinkedIn

```html
<!DOCTYPE html>
<html lang="en">
<head>
<meta charset="utf-8">
<title>Fenmoor Lift Brochure</title>
<link href="https://fonts.googleapis.com/css2?family=Open+Sans:wght@400;600;700;800&family=Montserrat:wght@600;700;800&display=swap" rel="stylesheet">
<style>
:root{
  --navy:#0b2a4a;
  --navy-deep:#071c33;
  --blue:#1b6fb5;
  --sky:#3ea3dc;
  --pale:#e9eef3;
  --stage:#eceff2;
  --ink:#1d2c3b;
  --muted:#5a6b7c;
  --sunset-a:#f5a13a;
  --sunset-b:#b5461b;
  --white:#ffffff;
}
*{margin:0;padding:0;box-sizing:border-box}
html,body{width:889px;height:1200px;overflow:hidden}
body{background:var(--stage);font-family:"Open Sans",sans-serif;color:var(--ink);position:relative}
.side-label{position:absolute;left:14px;font:600 15px "Open Sans",sans-serif;color:#555;transform:rotate(-90deg);transform-origin:left top;letter-spacing:.5px}
.side-label.front{top:370px}
.side-label.back{top:1020px}
.spread{position:absolute;left:60px;width:800px;box-shadow:0 2px 8px rgba(0,0,0,.18);overflow:hidden}
.spread.front{top:15px;height:525px;background:var(--white)}
.spread.back{top:605px;height:535px;background:var(--navy)}
.panel{position:absolute;top:0;height:100%;width:400px;overflow:hidden}
.panel.left{left:0}.panel.right{left:400px}
.abs{position:absolute}
.photo{position:absolute}
/* front left contact blocks */
.contact{position:absolute;left:100px;width:220px;text-align:center;font-size:8px;line-height:1.45;color:var(--ink)}
.contact .mark{display:block;width:12px;height:12px;margin:0 auto 4px;border-radius:50%;background:var(--blue)}
.contact strong{font-weight:700;color:var(--navy)}
/* front right */
.brand{position:absolute;left:0;width:400px;top:300px;text-align:center}
.brand .name{font:800 40px "Montserrat",sans-serif;color:var(--navy);letter-spacing:.5px;display:inline-flex;align-items:center;gap:10px}
.brand .dot{width:16px;height:16px;border-radius:50%;background:var(--sky);display:inline-block}
.web{position:absolute;left:0;width:400px;text-align:center;font:700 13px "Montserrat",sans-serif;letter-spacing:2px}
.front .web{top:492px;color:var(--navy)}
/* back */
.col{position:absolute;color:#dbe6f1;font-size:7.4px;line-height:1.45}
.col h3{font:800 8px "Montserrat",sans-serif;color:var(--sky);margin:8px 0 3px;letter-spacing:.3px}
.col p{margin-bottom:4px}
.col ul{list-style:none}
.col li{padding-left:9px;position:relative;margin-bottom:2px}
.col li::before{content:"";position:absolute;left:0;top:3px;width:4px;height:4px;background:var(--sky);border-radius:50%}
.boxed{background:var(--navy-deep);border-left:3px solid var(--sky);padding:6px 10px}
.back .web{bottom:7px;color:var(--white);font-size:12px}
.back-bar{position:absolute;left:0;right:0;bottom:0;height:28px;background:var(--navy-deep)}
.mini-brand{position:absolute;right:16px;bottom:36px;font:800 12px "Montserrat",sans-serif;color:var(--white);display:flex;align-items:center;gap:5px}
.mini-brand .dot{width:7px;height:7px;border-radius:50%;background:var(--sky)}
</style>
</head>
<body>
<div class="side-label front">Frontside</div>
<div class="side-label back">Backside</div>

<section class="spread front">
  <div class="panel left">
    <div class="contact" style="top:40px"><span class="mark"></span><strong>Address</strong><br>Unit Q8 Harlow Yard, Lydden Avenue<br>London SE1 4HG</div>
    <div class="contact" style="top:120px"><span class="mark"></span><strong>Telephone</strong><br>020 7958 2316</div>
    <div class="contact" style="top:190px"><span class="mark"></span><strong>E-mail</strong><br>enquiries@fenmoor-lift.com</div>
    <svg class="abs" style="left:0;top:300px" width="400" height="225" viewBox="0 0 400 225">
      <path d="M0 30 C120 0 260 10 400 70 L400 225 L0 225Z" fill="var(--blue)"/>
      <path d="M0 40 C120 12 260 22 400 82" fill="none" stroke="var(--sky)" stroke-width="4"/>
    </svg>
    <div class="photo" role="img" aria-label="Wind turbines against a blue sky" style="left:20px;top:345px;width:165px;height:100px;background:linear-gradient(180deg,#6fb0e0,#cfe4f4)"></div>
    <div class="photo" role="img" aria-label="Wind farm with turbines on grassland" style="left:200px;top:370px;width:180px;height:110px;background:linear-gradient(180deg,#8cc4ec,#d8e9f5 70%,#9bb58a)"></div>
    <div class="photo" role="img" aria-label="Row of wind turbines at sea" style="left:20px;top:455px;width:165px;height:60px;background:linear-gradient(180deg,#a7cdea,#4f7fa8)"></div>
  </div>
  <div class="panel right">
    <div class="photo" role="img" aria-label="Wind turbines silhouetted against an orange sunset" style="left:0;top:0;width:400px;height:260px;background:linear-gradient(180deg,#3a2a3a,var(--sunset-b) 45%,var(--sunset-a) 80%,#f6c66a)"></div>
    <svg class="abs" style="left:0;top:200px" width="400" height="120" viewBox="0 0 400 120">
      <path d="M0 40 C140 110 280 0 400 30 L400 120 L0 120Z" fill="var(--white)"/>
      <path d="M0 34 C140 100 280 -8 400 22" fill="none" stroke="var(--blue)" stroke-width="8"/>
      <path d="M0 46 C140 112 280 4 400 34" fill="none" stroke="var(--sky)" stroke-width="3"/>
    </svg>
    <svg class="abs" style="left:0;top:480px" width="400" height="45" viewBox="0 0 400 45">
      <path d="M0 10 C150 40 300 0 400 12 L400 45 L0 45Z" fill="var(--pale)"/>
    </svg>
    <div class="brand"><span class="name"><span class="dot"></span>Fenmoor Lift</span></div>
    <div class="web">WWW.FENMOOR-LIFT.UK</div>
  </div>
</section>

<section class="spread back">
  <div class="panel left">
    <div class="col" style="left:18px;top:4px;width:365px">
      <h3>VERTICAL INDUSTRIAL ROPE ACCESS</h3>
      <p>Our trained technicians reach every part of the blade by rope access, giving fast set up, low cost and minimal downtime for operators.</p>
      <p>All work follows industry guidance and is planned around site conditions, weather limits and turbine availability.</p>
      <h3>BRIDGING AND EXTENSION ROTOR BLADE SOLUTIONS</h3>
      <p>Where rope access alone is not enough we add platforms and extension systems to reach the root, tip and trailing edge safely.</p>
    </div>
    <div class="photo" role="img" aria-label="Technician on ropes working on a turbine blade" style="left:18px;top:150px;width:150px;height:165px;background:linear-gradient(180deg,#7fb5dd,#dbe9f4)"></div>
    <div class="col" style="left:180px;top:160px;width:205px">
      <h3>ROTOR BLADE &amp; OTHER INSPECTIONS</h3>
      <ul><li>Visual and tap testing of the full blade</li><li>Leading edge erosion surveys</li><li>Lightning receptor checks</li><li>Photo reports with repair advice</li><li>Tower and nacelle inspections</li></ul>
    </div>
    <div class="col boxed" style="left:18px;top:335px;width:170px">
      <h3 style="margin-top:0">COMPOSITE FIBRE BLADE REPAIRS</h3>
      <ul><li>Leading edge protection</li><li>Laminate and core repair</li><li>Crack and split repair</li><li>Filler and paint finish</li></ul>
    </div>
    <div class="photo" role="img" aria-label="Offshore wind turbines" style="left:200px;top:335px;width:185px;height:85px;background:linear-gradient(180deg,#8fc0e6,#3e6f98)"></div>
    <div class="photo" role="img" aria-label="Turbine blade close up" style="left:200px;top:425px;width:90px;height:70px;background:linear-gradient(180deg,#b9d7ee,#6c93b5)"></div>
    <div class="photo" role="img" aria-label="Turbines on a hillside" style="left:295px;top:425px;width:90px;height:70px;background:linear-gradient(180deg,#a4cbe8,#7f9d6e)"></div>
  </div>
  <div class="panel right">
    <div class="col" style="left:16px;top:4px;width:365px">
      <h3>CLEANING OF ROTOR BLADES AND TURBINE TOWERS</h3>
      <p>We remove oil, dirt and insect build up from blades and towers, restoring clean surfaces and aerodynamic performance.</p>
      <h3>COMPOSITE REPAIRS TO ROTOR BLADES AND TURBINE TOWERS</h3>
      <p>Damage is repaired in place with approved resin systems, cured and finished to the maker's standard.</p>
    </div>
    <div class="photo" role="img" aria-label="Repair work on a blade surface" style="left:16px;top:100px;width:110px;height:80px;background:linear-gradient(180deg,#c9dced,#7c98b2)"></div>
    <div class="col" style="left:136px;top:96px;width:245px">
      <h3>LIGHTNING PROTECTION SYSTEM</h3>
      <p>We test and repair receptors, down conductors and connections so each blade stays protected through the season.</p>
    </div>
    <div class="photo" role="img" aria-label="Wind turbines at dusk" style="left:16px;top:195px;width:365px;height:140px;background:linear-gradient(180deg,#36597d,#8fb6d6)"></div>
    <div class="col" style="left:16px;top:342px;width:365px">
      <h3>HEALTH AND SAFETY</h3>
      <p>Safety comes first on every job. Our teams hold current certificates and work to written method statements.</p>
      <h3>CONTACT</h3>
      <p>Unit Q8 Harlow Yard, Lydden Avenue, London SE1 4HG<br>Tel: 020 7958 2316 &nbsp; E-mail: enquiries@fenmoor-lift.com</p>
    </div>
    <div class="mini-brand"><span class="dot"></span>Fenmoor Lift</div>
  </div>
  <div class="back-bar"></div>
  <div class="web" style="left:0">WWW.FENMOOR-LIFT.UK</div>
  <div class="web" style="left:400px">WWW.FENMOOR-LIFT.UK</div>
</section>
</body>
</html>
```